Business Card Layout and Stationary Layout
Business Card Layout and Stationary Layout -
Creative Brief
Use same font as used in my logo
CHANGE THE FONT TO SOMETHING NEW
Professional
Paul Dawson
P.O. Box 31842 Seattle WA 98173
Paul@Brintacor.com
Brintacor.com
We need a new font. Something where we can have BRINTACOR used just in font form. We love our logo, but we want a more creative high-powered, stand-alone font. We also need a letterhead layout and an invoice layout. Will pay winner an extra $50 for these two items.

```html
<!DOCTYPE html>
<html lang="en">
<head>
<meta charset="utf-8">
<title>Brintacor Business Card</title>
<link href="https://fonts.googleapis.com/css2?family=Exo+2:wght@600;800&family=Open+Sans:wght@400;600&display=swap" rel="stylesheet">
<style>
  :root {
    --bg: #e9ebe8;
    --card: #ffffff;
    --green: #2f9a35;
    --green-dark: #1d6f24;
    --green-light: #dff0dc;
    --grey: #c9cccb;
    --text-dark: #2d3a2e;
    --text-muted: #6b7a6c;
  }
  * { margin: 0; padding: 0; box-sizing: border-box; }
  html, body { width: 1200px; height: 646px; overflow: hidden; background: var(--bg); }
  .stage { position: relative; width: 1200px; height: 646px; }
  .card {
    position: absolute; top: 168px; width: 540px; height: 310px;
    background: var(--card); border-radius: 4px; overflow: hidden;
    box-shadow: 0 6px 18px rgba(0,0,0,.16);
  }
  .card-back { left: 40px; }
  .card-front { left: 620px; }
  .card svg.shapes { position: absolute; inset: 0; }
  .brand {
    font-family: "Exo 2", sans-serif; font-weight: 800; color: var(--green);
    display: flex; align-items: center; gap: 12px; position: absolute; white-space: nowrap;
  }
  .brand-dot { width: 28px; height: 28px; border-radius: 50%; background: var(--green); flex: none; }
  .card-back .brand { font-size: 58px; left: 0; right: 0; top: 100px; justify-content: center; }
  .back-web {
    position: absolute; left: 0; right: 0; top: 190px; text-align: center;
    font-family: "Open Sans", sans-serif; font-size: 15px; color: var(--text-muted); letter-spacing: .5px;
  }
  .card-front .brand { font-size: 38px; left: 44px; top: 140px; }
  .holder {
    position: absolute; right: 26px; top: 20px;
    font-family: "Open Sans", sans-serif; font-weight: 600; font-size: 14px; color: var(--green-dark);
  }
  .contact {
    position: absolute; right: 26px; top: 62px; list-style: none; text-align: right;
    font-family: "Open Sans", sans-serif; font-size: 11px; line-height: 20px; color: #fff;
  }
  .contact li { display: flex; justify-content: flex-end; align-items: center; gap: 6px; }
  .contact svg { width: 11px; height: 11px; flex: none; }
</style>
</head>
<body>
<main class="stage">
  <section class="card card-back" aria-label="Card back">
    <svg class="shapes" viewBox="0 0 540 310" preserveAspectRatio="none">
      <path d="M0 0 H540 V40 C420 10 300 90 170 70 C90 58 30 40 0 60 Z" fill="var(--green-light)"/>
      <path d="M0 60 C30 40 90 58 170 70 C300 90 420 10 540 40 V52 C420 24 300 104 170 84 C90 72 30 56 0 74 Z" fill="var(--grey)" opacity=".5"/>
    </svg>
    <div class="brand">Brintacor</div>
    <p class="back-web">www.Brintacor.com</p>
  </section>

  <section class="card card-front" aria-label="Card front">
    <svg class="shapes" viewBox="0 0 540 310" preserveAspectRatio="none">
      <path d="M400 0 H540 V310 H0 V280 C280 270 400 220 400 0 Z" fill="var(--grey)"/>
      <path d="M418 0 H540 V310 H0 V296 C300 288 418 230 418 0 Z" fill="var(--green)"/>
      <path d="M500 0 H540 V310 H140 C380 290 490 200 500 0 Z" fill="var(--green-dark)" opacity=".3"/>
      <rect x="418" y="0" width="122" height="48" fill="var(--card)"/>
    </svg>
    <p class="holder">Paul Dawson</p>
    <div class="brand"><span class="brand-dot"></span>Brintacor</div>
    <ul class="contact">
      <li>P.O. Box 31842</li>
      <li>Seattle WA 98173</li>
      <li>206-555-0148
        <svg viewBox="0 0 12 12"><path d="M3 1 L5 3.5 L4 5 Q5.5 7 7 8 L8.5 7 L11 9 L9.5 11 Q4 10 1 2.5 Z" fill="#fff"/></svg></li>
      <li>Paul@Brintacor.com
        <svg viewBox="0 0 12 12"><rect x="1" y="3" width="10" height="7" fill="none" stroke="#fff"/><path d="M1 3 L6 7 L11 3" fill="none" stroke="#fff"/></svg></li>
      <li>Brintacor.com
        <svg viewBox="0 0 12 12"><circle cx="6" cy="6" r="5" fill="none" stroke="#fff"/><path d="M1 6 H11 M6 1 V11" stroke="#fff"/></svg></li>
    </ul>
  </section>
</main>
</body>
</html>
```